*Business Card Concept For Gum (Pollution) Removal Company*
Pave Pals
*Business Card Concept For Gum (Pollution) Removal Company* - Cleaning
Creative Brief
Bright & Fun-filled
Rutger Ashdown
President
582 Willow Crest Ave. Suite K Marlow Bay, Oregon 97341
1-800-615-PAVPALS (7287)
541-419-3068 Direct
info@pave-pals.example
www.pave-pals.example
Thank you for considering this project. This business card will represent my company that specializes in gum pollution removal. The next time you go to a busy shopping center or high traffic area, you might notice several unsightly black dots on the pavement. Typically they are near waste baskets. My company has a solution to removal such pollution. When designing the card I would like to include a visual element including "sticky" bubble gum and possibly variation of black dots on the pavement. If you are unclear about the "black dots", please google "chewing gum black dots". Thank you!

```html
<!DOCTYPE html>
<html lang="en">
<head>
<meta charset="utf-8">
<title>Pave Pals — Business Card</title>
<link href="https://fonts.googleapis.com/css2?family=Open+Sans:wght@400;600;800&display=swap" rel="stylesheet">
<style>
  :root {
    --pink: #e5168f;
    --pink-light: #f43fab;
    --pink-deep: #c80f7c;
    --ink: #3a3a3a;
    --muted: #6b6b6b;
    --paper: #ffffff;
    --backdrop: #d9d9d9;
  }
  * { box-sizing: border-box; margin: 0; padding: 0; }
  html, body { width: 1200px; height: 895px; overflow: hidden; }
  body {
    background: var(--backdrop);
    font-family: "Open Sans", Arial, sans-serif;
    color: var(--ink);
    display: flex;
    flex-direction: column;
    align-items: center;
    justify-content: center;
    gap: 36px;
  }
  .card {
    position: relative;
    width: 700px;
    height: 400px;
    overflow: hidden;
    box-shadow: 0 6px 18px rgba(0,0,0,.18);
  }

  /* Front */
  .card-front { background: var(--paper); }
  .edge-band { position: absolute; left: 0; right: 0; height: 14px; background: var(--pink); }
  .edge-band.top { top: 0; }
  .edge-band.bottom { bottom: 0; }
  .brand-block {
    position: absolute; left: 36px; top: 48px; width: 270px;
    display: flex; flex-direction: column; align-items: center;
  }
  .worker-illustration {
    width: 150px; height: 150px; border-radius: 6px;
    background: linear-gradient(160deg, var(--pink-light), var(--pink-deep));
  }
  .brand-name {
    margin-top: 10px;
    font-weight: 800; font-size: 46px; line-height: 1;
    color: var(--pink); text-transform: uppercase; letter-spacing: .5px;
  }
  .brand-tagline { margin-top: 8px; font-size: 12px; font-weight: 600; color: var(--ink); }
  .divider {
    position: absolute; left: 326px; top: 70px; bottom: 70px;
    width: 1px; background: #bdbdbd;
  }
  .contact-block { position: absolute; left: 350px; top: 96px; right: 30px; }
  .person-name { font-size: 22px; font-weight: 600; color: var(--pink); }
  .person-title { font-size: 14px; color: var(--muted); margin-bottom: 16px; }
  .contact-list { list-style: none; }
  .contact-list li {
    display: flex; align-items: flex-start; gap: 9px;
    font-size: 12.5px; line-height: 1.4; margin-bottom: 5px;
  }
  .contact-icon {
    flex: none; width: 16px; height: 16px; border-radius: 50%;
    background: var(--pink); margin-top: 1px;
    display: flex; align-items: center; justify-content: center;
  }
  .contact-icon svg { width: 10px; height: 10px; fill: #fff; }

  /* Back */
  .card-back {
    background: radial-gradient(circle at 50% 45%, var(--pink-light) 0%, var(--pink) 55%, var(--pink-deep) 100%);
  }
  .back-brand { position: absolute; left: 44px; top: 70px; color: #fff; }
  .back-brand .brand-name { color: #fff; font-size: 50px; margin: 0; line-height: .95; }
  .back-brand .brand-tagline { color: #fff; font-size: 12px; margin-top: 8px; }
  .back-illustration {
    position: absolute; right: 50px; bottom: 60px; width: 250px; height: 230px;
    border-radius: 8px;
    background: linear-gradient(170deg, rgba(255,255,255,.35), rgba(255,255,255,.12));
  }
</style>
</head>
<body>

  <section class="card card-front">
    <div class="edge-band top"></div>
    <div class="brand-block">
      <div class="worker-illustration" role="img" aria-label="Illustration of a worker cleaning pavement with a vacuum wand"></div>
      <div class="brand-name">Pave Pals</div>
      <div class="brand-tagline">Your Pavement Spot Cleanup Crew</div>
    </div>
    <div class="divider"></div>
    <div class="contact-block">
      <div class="person-name">Rutger Ashdown</div>
      <div class="person-title">President</div>
      <ul class="contact-list">
        <li><span class="contact-icon"><svg viewBox="0 0 10 10"><path d="M5 0.5a3.2 3.2 0 0 0-3.2 3.2C1.8 6 5 9.5 5 9.5S8.2 6 8.2 3.7A3.2 3.2 0 0 0 5 0.5zm0 4.4a1.2 1.2 0 1 1 0-2.4 1.2 1.2 0 0 1 0 2.4z"/></svg></span>
          <span>582 Willow Crest Ave. Suite K<br>Marlow Bay, Oregon 97341</span></li>
        <li><span class="contact-icon"><svg viewBox="0 0 10 10"><path d="M2.2 0.8l1.5 1.9-.9 1.1c.6 1.2 1.6 2.2 2.8 2.8l1.1-.9 1.9 1.5-.9 1.7C4.6 8.7 1.3 5.4 .5 1.7z"/></svg></span>
          <span>1-800-615-PAVPALS (7287)</span></li>
        <li><span class="contact-icon"><svg viewBox="0 0 10 10"><path d="M2.2 0.8l1.5 1.9-.9 1.1c.6 1.2 1.6 2.2 2.8 2.8l1.1-.9 1.9 1.5-.9 1.7C4.6 8.7 1.3 5.4 .5 1.7z"/></svg></span>
          <span>541-419-3068 Direct</span></li>
        <li><span class="contact-icon"><svg viewBox="0 0 10 10"><path d="M1 2.5h8v5H1z M1 2.5l4 3 4-3" fill="none" stroke="#fff" stroke-width="1"/></svg></span>
          <span>info@pave-pals.example</span></li>
        <li><span class="contact-icon"><svg viewBox="0 0 10 10"><circle cx="5" cy="5" r="3.8" fill="none" stroke="#fff" stroke-width="1"/><path d="M1.2 5h7.6M5 1.2c-2 2.4-2 5.2 0 7.6M5 1.2c2 2.4 2 5.2 0 7.6" fill="none" stroke="#fff" stroke-width=".8"/></svg></span>
          <span>www.pave-pals.example</span></li>
      </ul>
    </div>
    <div class="edge-band bottom"></div>
  </section>

  <section class="card card-back">
    <div class="back-brand">
      <div class="brand-name">Pave<br>Pals</div>
      <div class="brand-tagline">Pavement Spot Cleanup Crew</div>
    </div>
    <div class="back-illustration" role="img" aria-label="Illustration of a worker in a cap vacuuming gum spots off the pavement"></div>
  </section>

</body>
</html>
```